VELMAR WEBSITE

need to create a new website for VELMAR ltd
the company deals with all aspects of safety products & safety wear
we need a simple website to show
ideas can be taken from following website whose products we shall distribute in kenya
www.qtw.co.uk
www.brovik.eu
www.tormanhardgear.com
www.qalvenworks.co.za

we need following tabs
1) home - basic company information
2) products - broken down to following categories ie gloves, head protection, ear protection, mouth protection, foot protection
3) contacts

the company profile is a reputable company dealing with all aspects of safety, HSE (health and safety equipment), and PPE (personal protective equipment)

the website should have the brovik logo for which we are an authorized distributor.
the brovi industrial range writeup can be picked from their website

Dear Designers, i shall be able to choose a final design in 2 weeks, sorry i have not been able to finalise this due to a personal reason

Target Market(s)

the buyers are all types of industry who care for their employees safety

Industry/Entity Type

Industrial

Requirements
Must have
• clean look, fresh look, user freindly
Nice to have
• clear images, quick links etc

```html
<!DOCTYPE html>
<html lang="en">
<head>
<meta charset="utf-8">
<title>VELMAR — Safety Products &amp; Safety Wear</title>
<link rel="stylesheet" href="https://fonts.googleapis.com/css2?family=Advent+Pro:wght@300;400;500&family=Merriweather:wght@400;700&family=Open+Sans:wght@400;600;700&display=swap">
<style>
:root{
  --orange:#f7a823;
  --teal:#0f3a4a;
  --ink:#111111;
  --white:#ffffff;
  --muted:#8a8a8a;
  --title:#1d3f4f;
}
*{box-sizing:border-box;margin:0;padding:0}
html,body{width:1200px;height:2235px;overflow:hidden;background:var(--white)}
body{position:relative;font-family:"Open Sans",Arial,sans-serif;color:var(--ink)}
.abs{position:absolute}

/* hero */
.hero{left:0;top:0;width:1200px;height:715px;
  background:radial-gradient(ellipse at 52% 50%,#f3b560 0%,#b0683a 14%,#3e3a45 38%,#1b2a3c 70%,#0f1b2a 100%)}
.navbar{left:0;top:67px;width:1200px;height:62px;background:var(--orange)}
.nav-link{top:87px;font-size:16px;color:var(--white);white-space:nowrap}
.menu-icon{left:1124px;top:89px;width:20px;height:18px}
.brand-box{left:100px;top:40px;width:240px;height:180px;background:var(--white);
  box-shadow:0 2px 6px rgba(0,0,0,.35);display:flex;align-items:center;justify-content:center;gap:12px}
.brand-mark{width:26px;height:26px;background:var(--orange)}
.brand-name{font-family:"Open Sans",Arial,sans-serif;font-weight:700;font-size:40px;color:var(--teal);letter-spacing:1px}
.headline{left:100px;top:346px;font-family:"Merriweather",Georgia,serif;font-weight:400;font-size:49px;line-height:58px;color:var(--white);
  text-shadow:0 2px 4px rgba(0,0,0,.5);letter-spacing:2.5px;white-space:nowrap}
.join-btn{left:100px;top:485px;width:262px;height:49px;border:3px solid var(--white);color:var(--white);
  font-family:"Advent Pro",Arial,sans-serif;font-size:28px;letter-spacing:2px;display:flex;align-items:center;justify-content:center}
.slide-arrow{top:585px;width:49px;height:41px;background:var(--orange);display:flex;align-items:center;justify-content:center}

/* welcome */
.welcome{left:0;top:715px;width:1200px;height:230px;background:var(--teal)}
.welcome-label{left:512px;top:760px;width:212px;height:56px;background:var(--orange);
  font-family:"Advent Pro",Arial,sans-serif;font-weight:400;font-size:44px;color:var(--teal);display:flex;align-items:center;justify-content:center}
.welcome-text{left:40px;top:834px;width:1120px;text-align:center;font-family:"Advent Pro",Arial,sans-serif;
  font-weight:400;font-size:25px;line-height:26px;color:#e5ecef;letter-spacing:.3px}

/* products */
.section-title{left:0;top:1012px;width:1200px;text-align:center;font-family:"Advent Pro",Arial,sans-serif;
  font-weight:400;font-size:48px;color:var(--title)}
.product{width:280px}
.product-photo{width:264px;height:208px;margin:0 auto}
.product-name{margin-top:22px;text-align:center;font-weight:700;font-size:17px;letter-spacing:.5px}
.product-desc{margin:4px auto 0;width:250px;text-align:center;font-size:11px;line-height:12.5px;color:var(--muted)}
.shop-btn{margin:14px auto 0;width:199px;height:39px;background:var(--ink);color:var(--white);
  font-family:"Advent Pro",Arial,sans-serif;font-weight:500;font-size:22px;display:flex;align-items:center;justify-content:center;gap:18px}
.shop-btn::before{content:"";width:7px;height:7px;border-radius:50%;background:var(--orange)}

/* footer */
.footer{left:0;top:1971px;width:1200px;height:237px;background:var(--teal)}
.footer-col h3{font-family:"Open Sans",Arial,sans-serif;font-weight:600;font-size:21px;color:var(--white);margin-bottom:12px}
.footer-col a{display:block;color:var(--white);text-decoration:none;font-size:16px;line-height:27px}
.connect-title{left:858px;top:2019px;font-weight:600;font-size:21px;color:var(--white)}
.socials{left:836px;top:2074px;display:flex;gap:8px}
.social{font-size:11px;color:var(--white);display:flex;align-items:center;gap:3px}
.social::before{content:"";width:9px;height:9px;border-radius:50%;background:var(--white)}
.cta-btn{left:847px;top:2123px;width:228px;height:45px;background:var(--orange);border-radius:4px;
  color:var(--teal);font-weight:700;font-size:17px;display:flex;align-items:center;justify-content:center}
.bottom-bar{left:0;top:2208px;width:1200px;height:27px;background:var(--orange)}
.copyright{left:10px;top:2214px;font-size:11px;font-weight:600;color:var(--ink)}
</style>
</head>
<body>

<header>
  <div class="abs hero" role="img" aria-label="Industrial refinery at sunset with pipelines stretching toward the glowing horizon"></div>
  <div class="abs navbar"></div>
  <nav>
    <span class="abs nav-link" style="left:422px">Service Directory</span>
    <span class="abs nav-link" style="left:599px">News &amp; Events</span>
    <span class="abs nav-link" style="left:764px">About us</span>
    <span class="abs nav-link" style="left:885px">Products</span>
    <span class="abs nav-link" style="left:1006px">Branches</span>
    <svg class="abs menu-icon" viewBox="0 0 20 18" aria-label="Menu"><rect y="1" width="20" height="3" fill="#fff"/><rect y="7.5" width="20" height="3" fill="#fff"/><rect y="14" width="20" height="3" fill="#fff"/></svg>
  </nav>
  <div class="abs brand-box"><span class="brand-mark"></span><span class="brand-name">VELMAR</span></div>
  <h1 class="abs headline">push harder than yesterday…<br>if you want a better tomorrow!</h1>
  <div class="abs join-btn">JOIN US</div>
  <div class="abs slide-arrow" style="left:100px"><svg width="14" height="20" viewBox="0 0 14 20"><path d="M11 2 3 10l8 8" fill="none" stroke="#111" stroke-width="3"/></svg></div>
  <div class="abs slide-arrow" style="left:156px"><svg width="14" height="20" viewBox="0 0 14 20"><path d="M3 2l8 8-8 8" fill="none" stroke="#111" stroke-width="3"/></svg></div>
</header>

<section>
  <div class="abs welcome"></div>
  <h2 class="abs welcome-label">Welcome!</h2>
  <p class="abs welcome-text">The magic chain wine holder is a perfect gift for any wine enthusiast. The chain is nickel-plated iron<br>which appears to defy the laws of physics. Fits any normal size wine bottle.</p>
</section>

<section>
  <h2 class="abs section-title">Product Categories</h2>

  <article class="abs product" style="left:81px;top:1129px">
    <div class="product-photo" style="background:linear-gradient(135deg,#2b3a30,#7c8f6a 55%,#c9ccc2)" role="img" aria-label="Gloved hand gripping a steel pipe"></div>
    <h3 class="product-name">HAND PROTECTION</h3>
    <p class="product-desc">Harlow Recruitment Partners is recognised as one of the leading providers and growing demand for talent.</p>
    <div class="shop-btn">SHOP HERE</div>
  </article>
  <article class="abs product" style="left:464px;top:1129px">
    <div class="product-photo" style="background:linear-gradient(135deg,#3a3326,#2a3b5a 55%,#b8a58a)" role="img" aria-label="Worker in hard hat and safety glasses using a hammer"></div>
    <h3 class="product-name">EYE AND FACE PROTECTION</h3>
    <p class="product-desc">Harlow Recruitment Partners is recognised as one of the leading providers and growing demand for talent.</p>
    <div class="shop-btn">SHOP HERE</div>
  </article>
  <article class="abs product" style="left:840px;top:1129px">
    <div class="product-photo" style="background:linear-gradient(160deg,#d7e2ee,#a9b8c8 55%,#5b5048)" role="img" aria-label="Worker in harness climbing a steel structure"></div>
    <h3 class="product-name">FALL PROTECTION</h3>
    <p class="product-desc">Harlow Recruitment Partners is recognised as one of the leading providers and growing demand for talent.</p>
    <div class="shop-btn">SHOP HERE</div>
  </article>

  <article class="abs product" style="left:81px;top:1540px">
    <div class="product-photo" style="background:linear-gradient(135deg,#5a3b2a,#d8d6d2 50%,#8a6fa0)" role="img" aria-label="Worker in white coverall wearing a respirator mask"></div>
    <h3 class="product-name">GAS PROTECTION</h3>
    <p class="product-desc">Harlow Recruitment Partners is recognised as one of the leading providers and growing demand for talent.</p>
    <div class="shop-btn">SHOP HERE</div>
  </article>
  <article class="abs product" style="left:464px;top:1540px">
    <div class="product-photo" style="background:linear-gradient(135deg,#1f3a2c,#2f8a5e 55%,#0f1a14)" role="img" aria-label="Hands in green chemical gloves handling equipment"></div>
    <h3 class="product-name">HEARING PROTECTION</h3>
    <p class="product-desc">Harlow Recruitment Partners is recognised as one of the leading providers and growing demand for talent.</p>
    <div class="shop-btn">SHOP HERE</div>
  </article>
  <article class="abs product" style="left:840px;top:1540px">
    <div class="product-photo" style="background:linear-gradient(135deg,#8a4a2a,#34456a 50%,#1e2a3a)" role="img" aria-label="Worker in blue hard hat servicing machinery"></div>
    <h3 class="product-name">DISOPSABLE CLOTHING</h3>
    <p class="product-desc">Harlow Recruitment Partners is recognised as one of the leading providers and growing demand for talent.</p>
    <div class="shop-btn">SHOP HERE</div>
  </article>
</section>

<footer>
  <div class="abs footer"></div>
  <div class="abs footer-col" style="left:87px;top:2019px"><h3>OVERVIEW</h3><a>About Us</a><a>Features</a><a>Pricing</a><a>Examples</a></div>
  <div class="abs footer-col" style="left:331px;top:2019px"><h3>OVERVIEW</h3><a>About Us</a><a>Features</a><a>Pricing</a><a>Examples</a></div>
  <div class="abs footer-col" style="left:579px;top:2019px"><h3>OVERVIEW</h3><a>About Us</a><a>Features</a><a>Pricing</a><a>Examples</a></div>
  <div class="abs connect-title">STAY CONNECTED</div>
  <div class="abs socials">
    <span class="social">Chirply</span><span class="social">Linkora</span><span class="social">Vidnest</span><span class="social">Tagbox</span><span class="social">Circlo</span>
  </div>
  <div class="abs cta-btn">LETS GET STARTED</div>
  <div class="abs bottom-bar"></div>
  <div class="abs copyright">© VELMAR 2010 - 2013 ALL RIGHTS RESERVED</div>
</footer>

</body>
</html>
```